Customer Dashboard Design for Email Security SaaS

Mailbrook is a commercial email spam filter offered as a SaaS product, built and operated by a small German hosting provider. It protects business email accounts against spam, phishing, scam, and viruses using a multilayer filtering pipeline that combines traditional spam detection with AI-powered classification. The product runs entirely on German infrastructure, ensuring data sovereignty for European customers.

We need a complete redesign of the customer-facing dashboard. This is the web application where paying customers manage their email filtering: view their mail log, check quarantined emails, manage allow/blocklists, configure their settings, and handle their subscription. It is the primary touchpoint between Mailbrook and its customers.

Our customers are system administrators, IT managers at small-to-medium businesses, and operators of small hosting providers. They are technically competent but not designers. They expect professional, efficient tools that respect their time. They typically manage 10–500 email accounts and check the dashboard a few times per week, with heavier use during spam incidents.

We have attached the current mockups which really need to be replaced with something good looking.

Target Market(s)

System administrators, IT managers at small-to-medium businesses, and operators of small hosting providers.

Industry/Entity Type

SaaS

Number of Pages Required

5+ page

```html
<!DOCTYPE html>
<html lang="de">
<head>
<meta charset="utf-8">
<title>Mailbrook – Postfachkontingent</title>
<link href="https://fonts.googleapis.com/css2?family=Poppins:wght@400;500;600;700&display=swap" rel="stylesheet">
<style>
:root{
  --bg:#0b0f0d;
  --sidebar:#111613;
  --card:#141916;
  --card-2:#0e1210;
  --line:#242a26;
  --green:#22c56e;
  --green-dark:#0f2a1c;
  --avatar:#284634;
  --text:#ffffff;
  --muted:#8a918d;
  --danger:#e46a5a;
}
*{box-sizing:border-box;margin:0;padding:0}
html,body{width:1200px;height:1010px;overflow:hidden;background:var(--bg);color:var(--text);font-family:"Poppins",sans-serif}
.app{position:relative;width:1200px;height:1010px}
.topbar{position:absolute;left:0;top:0;width:1200px;height:58px;border-bottom:1px solid var(--line)}
.brand{position:absolute;left:0;top:0;width:232px;height:58px;border-right:1px solid var(--line);display:flex;align-items:center;padding-left:14px;gap:13px}
.brand-mark{width:42px;height:42px;border-radius:9px;background:var(--green)}
.brand-name{font-size:20px;font-weight:600}
.search{position:absolute;left:438px;top:11px;width:306px;height:36px;border:1px solid #2e3430;border-radius:18px;display:flex;align-items:center;padding:0 12px 0 19px;font-size:11.5px;color:var(--muted);justify-content:space-between}
.top-btn{position:absolute;top:13px;height:36px;border:1px solid #2a3a30;border-radius:5px;background:#101a14;display:flex;align-items:center;font-size:11.5px;letter-spacing:.3px}
.top-btn .ico{width:33px;height:100%;display:flex;align-items:center;justify-content:center;border-right:1px solid #2a3a30}
.top-btn span{padding:0 12px}
.user{position:absolute;left:1031px;top:10px;display:flex;align-items:center;gap:8px;font-size:12.5px;font-weight:500}
.user-photo{width:38px;height:38px;border-radius:50%;background:linear-gradient(135deg,#5c6b61,#a28a73)}
.sidebar{position:absolute;left:0;top:58px;width:232px;height:952px;background:var(--sidebar);border-right:1px solid var(--line)}
.nav-home{position:absolute;left:14px;top:15px;width:207px;height:39px;border-radius:5px;background:var(--green-dark);border-right:2px solid var(--green);display:flex;align-items:center;gap:6px;padding-left:4px;color:var(--green);font-weight:600;font-size:12.5px}
.nav-home .ico{width:33px;height:33px;border-radius:5px;background:#fff;display:flex;align-items:center;justify-content:center}
.nav-item{position:absolute;left:14px;width:204px;height:39px;display:flex;align-items:center;gap:13px;font-size:12px;border-bottom:1px solid var(--line)}
.nav-item:last-of-type{border-bottom:0}
.nav-admin{position:absolute;left:0;top:345px;width:232px;height:39px;background:var(--green-dark);border-right:3px solid var(--green);display:flex;align-items:center;gap:12px;padding-left:14px;font-size:12.5px;font-weight:500}
.main{position:absolute;left:260px;top:58px}
h1{position:absolute;left:0;top:28px;font-size:25px;font-weight:600;white-space:nowrap}
.lead{position:absolute;left:3px;top:66px;font-size:12.5px;white-space:nowrap;color:#e6e8e7}
.usage{position:absolute;left:4px;top:108px;width:910px;height:143px;background:var(--card);border:1px solid var(--line);border-radius:12px}
.usage h2{position:absolute;left:15px;top:12px;font-size:17px;font-weight:600}
.sync{position:absolute;left:15px;top:42px;font-size:11.5px;display:flex;align-items:center;gap:4px}
.count{position:absolute;left:15px;top:70px;width:218px;height:63px;background:var(--card-2);border:1px solid var(--line);border-radius:6px;display:flex;align-items:center;padding-left:13px;gap:14px}
.count b{font-size:36px;font-weight:700}
.count small{font-size:20px;font-weight:500}
.count .pill{font-size:11.5px;font-weight:500;display:flex;align-items:center;gap:5px}
.ring{position:absolute;left:272px;top:12px}
.threshold{position:absolute;left:422px;top:41px;width:466px;height:63px;background:var(--card-2);border:1px solid var(--line);border-radius:6px}
.threshold .row{position:absolute;left:15px;top:14px;display:flex;align-items:center;gap:8px;font-size:12.5px;font-weight:500}
.dot{width:10px;height:10px;border-radius:50%;background:var(--green)}
.tag{border:1px solid #2e3430;border-radius:10px;padding:2px 8px;font-size:8.5px;display:flex;align-items:center;gap:4px;margin-left:6px}
.bar{position:absolute;left:19px;top:43px;width:433px;height:3px;background:#2a302c;border-radius:2px}
.bar i{display:block;width:47%;height:3px;background:var(--green);border-radius:2px}
h3{position:absolute;left:4px;top:280px;font-size:24px;font-weight:600;display:flex;align-items:center;gap:8px;white-space:nowrap}
h3 .mailbox{width:22px;height:20px;border-radius:3px;background:linear-gradient(#4a7fbf,#2f5b92)}
.grid{position:absolute;left:4px;top:327px;width:911px;display:grid;grid-template-columns:448px 448px;column-gap:15px;row-gap:15px}
.box{position:relative;height:72px;background:var(--card);border:1px solid var(--line);border-radius:7px;display:flex;align-items:center;padding-left:10px;gap:10px}
.box.hover{border-color:var(--green)}
.initials{width:39px;height:39px;border-radius:50%;background:var(--avatar);display:flex;align-items:center;justify-content:center;font-weight:600;font-size:13.5px}
.addr{font-size:15px;line-height:1.2}
.meta{margin-top:6px;font-size:11px;color:var(--muted);display:flex;align-items:center;gap:5px}
.remove{position:absolute;right:11px;top:22px;height:28px;padding:0 10px;border:1px solid #6a2a22;background:#2a1612;border-radius:14px;font-size:8px;letter-spacing:.4px;display:flex;align-items:center;gap:5px;color:#f1c8c0}
.scroll{position:absolute;left:927px;top:327px;width:4px;height:513px;background:#1c221e;border-radius:2px}
.scroll i{display:block;margin-top:20px;height:63px;background:var(--green);border-radius:2px}
.adder{position:absolute;left:4px;top:853px;width:910px;height:72px;background:#0f1d15;border:1px dashed #2f5a40;border-radius:7px}
.adder .input{position:absolute;left:17px;top:17px;width:396px;height:41px;border:1px solid #2e3430;border-radius:20px;background:#0c130f;font-size:11.5px;color:var(--muted);display:flex;align-items:center;padding-left:19px}
.plan{position:absolute;left:486px;top:17px;width:177px;height:37px;border:1px solid #3a4a40;border-radius:19px;display:flex;align-items:center;justify-content:center;gap:6px;font-size:12.5px;color:#cfd3d1}
.plan b{color:#fff;font-weight:500}
.add-btn{position:absolute;left:673px;top:17px;width:221px;height:37px;border-radius:19px;background:var(--green);display:flex;align-items:center;justify-content:center;font-size:13px;font-weight:500}
</style>
</head>
<body>
<div class="app">
  <header class="topbar">
    <div class="brand"><div class="brand-mark"></div><div class="brand-name">Mailbrook</div></div>
    <div class="search">Hier suchen
      <svg width="16" height="16" viewBox="0 0 24 24" fill="none" stroke="#fff" stroke-width="2.5"><circle cx="10" cy="10" r="7"/><path d="M15 15l6 6"/></svg></div>
    <div class="top-btn" style="left:766px;width:134px"><div class="ico"><svg width="13" height="16" viewBox="0 0 14 18"><rect x="1" y="7" width="12" height="10" rx="1.5" fill="#fff"/><path d="M3.5 7V5a3.5 3.5 0 017 0v2" fill="none" stroke="#fff" stroke-width="2"/></svg></div><span>QUARANTÄNE</span></div>
    <div class="top-btn" style="left:910px;width:110px"><div class="ico"><svg width="17" height="12" viewBox="0 0 18 12"><rect width="18" height="12" rx="1.5" fill="#fff"/><path d="M1 1l8 6 8-6" fill="none" stroke="#101a14" stroke-width="1.5"/></svg></div><span>MAIL-LOG</span></div>
    <div class="user"><div class="user-photo" role="img" aria-label="Profilfoto des Nutzers"></div>Jonas Keller
      <svg width="12" height="8" viewBox="0 0 12 8" fill="none" stroke="#fff" stroke-width="1.8"><path d="M1 1l5 5 5-5"/></svg></div>
  </header>

  <nav class="sidebar">
    <div class="nav-home"><div class="ico"><svg width="22" height="20" viewBox="0 0 22 20"><path d="M11 1L1 10h3v9h5v-6h4v6h5v-9h3z" fill="#111"/></svg></div>ÜBERSICHT</div>
    <div class="nav-item" style="top:67px"><svg width="20" height="16" viewBox="0 0 20 16" fill="none" stroke="#fff" stroke-width="1.6"><rect x="1" y="1" width="18" height="14" rx="1"/><path d="M1 1l9 7 9-7M1 15l7-6M19 15l-7-6"/></svg>MAIL-LOG</div>
    <div class="nav-item" style="top:106px"><svg width="20" height="18" viewBox="0 0 20 18" fill="none" stroke="#fff" stroke-width="1.8"><path d="M1 9v8h18V9M1 9h5l1 3h6l1-3h5M7 4l2 2 5-5"/></svg>POSTFÄCHER</div>
    <div class="nav-item" style="top:145px"><svg width="20" height="20" viewBox="0 0 20 20" fill="none" stroke="#fff" stroke-width="1.8"><rect x="1" y="1" width="18" height="18" rx="4"/><circle cx="10" cy="10" r="5"/><path d="M7.5 10l2 2 3-3.5"/></svg>ALLOWLIST</div>
    <div class="nav-item" style="top:184px"><svg width="20" height="18" viewBox="0 0 20 18" fill="none" stroke="#fff" stroke-width="1.6"><rect x="1" y="1" width="16" height="12" rx="1"/><path d="M1 1l8 6 8-6"/><circle cx="15" cy="13" r="4" fill="#111613"/><path d="M12.5 10.5l5 5"/></svg>BLOCKLIST</div>
    <div class="nav-item" style="top:223px"><svg width="16" height="20" viewBox="0 0 14 18"><rect x="1" y="7" width="12" height="10" rx="1.5" fill="#fff"/><path d="M3.5 7V5a3.5 3.5 0 017 0v2" fill="none" stroke="#fff" stroke-width="2"/></svg>QUARANTÄNE</div>
    <div class="nav-item" style="top:262px"><svg width="20" height="20" viewBox="0 0 24 24"><path d="M12 2l2 3 3.5-1 .5 3.5 3.5.5-1 3.5 3 2-3 2 1 3.5-3.5.5-.5 3.5-3.5-1-2 3-2-3-3.5 1-.5-3.5L3 17.5l1-3.5-3-2 3-2-1-3.5L6.5 6 7 2.5 10.5 3.5z" fill="#fff"/><circle cx="12" cy="12" r="4" fill="#111613"/></svg>EINSTELLUNGEN</div>
    <div class="nav-item" style="top:301px"><svg width="22" height="20" viewBox="0 0 22 20" fill="none" stroke="#fff" stroke-width="1.8"><circle cx="4" cy="4" r="3"/><path d="M8 6h10v13H6V9M9 10h7M9 13h7M9 16h5M18 6l3-2"/></svg>ABRECHNUNG</div>
    <div class="nav-admin"><svg width="20" height="20" viewBox="0 0 24 24"><path d="M12 2l2 3 3.5-1 .5 3.5 3.5.5-1 3.5 3 2-3 2 1 3.5-3.5.5-.5 3.5-3.5-1-2 3-2-3-3.5 1-.5-3.5L3 17.5l1-3.5-3-2 3-2-1-3.5L6.5 6 7 2.5 10.5 3.5z" fill="#fff"/><circle cx="12" cy="12" r="5" fill="#0f2a1c"/><circle cx="12" cy="12" r="2.5" fill="#fff"/></svg>ADMINISTRATION</div>
  </nav>

  <main class="main">
    <h1>Postfachkontingent</h1>
    <p class="lead">Verwalten Sie Ihr E-Mail-Umfeld, überwachen Sie Nutzungsgrenzen und sorgen Sie für Ordnung in Ihrem beruflichen Umfeld.</p>

    <section class="usage">
      <h2>Lagerung &amp; Adressen</h2>
      <div class="sync"><svg width="12" height="12" viewBox="0 0 12 12" fill="none" stroke="#fff" stroke-width="1.4"><circle cx="6" cy="6" r="5"/><path d="M6 3v3l2 1"/></svg>Echtzeit-Synchronisierung</div>
      <div class="count"><div><b>12</b><small>/25</small></div>
        <div class="pill"><svg width="13" height="13" viewBox="0 0 14 14"><circle cx="7" cy="7" r="7" fill="#22c56e"/><path d="M4 7l2 2 4-4" fill="none" stroke="#0b0f0d" stroke-width="1.8"/></svg>Aktive Nutzung</div></div>
      <svg class="ring" width="122" height="122" viewBox="0 0 122 122">
        <circle cx="61" cy="61" r="55" fill="none" stroke="#3a3f3c" stroke-width="6"/>
        <circle cx="61" cy="61" r="55" fill="none" stroke="#22c56e" stroke-width="6" stroke-dasharray="166 346" transform="rotate(-90 61 61)"/>
        <text x="61" y="62" text-anchor="middle" font-family="Poppins,sans-serif" font-weight="700" font-size="38" fill="#fff">48</text>
        <text x="61" y="79" text-anchor="middle" font-family="Poppins,sans-serif" font-size="8" fill="#b8bdba">NUTZUNG</text>
        <rect x="12" y="88" width="98" height="18" rx="9" fill="#141916" stroke="#2e3430"/>
        <text x="61" y="100.5" text-anchor="middle" font-family="Poppins,sans-serif" font-size="8.5" fill="#fff">Noch 13 Adressen</text>
      </svg>
      <div class="threshold">
        <div class="row"><span class="dot"></span>Warnschwelle: 80 %
          <span class="tag"><svg width="8" height="9" viewBox="0 0 8 9"><path d="M4 0a3 3 0 013 3v3l1 1H0l1-1V3a3 3 0 013-3zM3 8h2a1 1 0 01-2 0z" fill="#fff"/></svg>Noch 13 Adressen – Sicherheitszone</span></div>
        <div class="bar"><i></i></div>
      </div>
    </section>

    <h3><span class="mailbox" role="img" aria-label="Briefkasten-Symbol"></span>Registrierte Postfächer</h3>

    <div class="grid">
      <div class="box hover"><div class="initials">JD</div><div><div class="addr">john.doe@company.com</div><div class="meta">▦ Created Jan 12, 2026</div></div>
        <div class="remove"><svg width="8" height="9" viewBox="0 0 8 9"><path d="M0 1.5h8M3 0h2M1 2.5h6l-.5 6.5h-5z" fill="#e46a5a" stroke="#e46a5a" stroke-width=".8"/></svg>ENTFERNEN</div></div>
      <div class="box"><div class="initials">AS</div><div><div class="addr">admin.support@company.com</div><div class="meta">▦ Created Jan 12, 2026</div></div></div>
      <div class="box"><div class="initials">HT</div><div><div class="addr">hr.team@company.com</div><div class="meta">▦ Created Jan 12, 2026</div></div></div>
      <div class="box"><div class="initials">LC</div><div><div class="addr">legal@company.com</div><div class="meta">▦ Created Jan 12, 2026</div></div></div>
      <div class="box"><div class="initials">PC</div><div><div class="addr">partners@company.com</div><div class="meta">▦ Created Jan 12, 2026</div></div></div>
      <div class="box"><div class="initials">EC</div><div><div class="addr">events@company.com</div><div class="meta">▦ Created Jan 12, 2026</div></div></div>
      <div class="box"><div class="initials">RC</div><div><div class="addr">research@company.com</div><div class="meta">▦ Created Jan 12, 2026</div></div></div>
      <div class="box"><div class="initials">JD</div><div><div class="addr">john.doe@company.com</div><div class="meta">▦ Created Jan 12, 2026</div></div></div>
      <div class="box"><div class="initials">IS</div><div><div class="addr">it.support@company.com</div><div class="meta">▦ Created Jan 12, 2026</div></div></div>
      <div class="box"><div class="initials">CC</div><div><div class="addr">compliance@company.com</div><div class="meta">▦ Created Jan 12, 2026</div></div></div>
      <div class="box"><div class="initials">CC</div><div><div class="addr">customer.care@company.com</div><div class="meta">▦ Created Jan 12, 2026</div></div></div>
      <div class="box"><div class="initials">PC</div><div><div class="addr">product@company.com</div><div class="meta">▦ Created Jan 12, 2026</div></div></div>
    </div>
    <div class="scroll"><i></i></div>

    <div class="adder">
      <div class="input">new@domain.com</div>
      <div class="plan"><span class="dot"></span>Tarif: <b>Pro Enterprise</b></div>
      <div class="add-btn">+ E-Mail-Adresse hinzufügen</div>
    </div>
  </main>
</div>
</body>
</html>
```